Emergency Medical Training and Events Company Business Needs Business Card Design

We are in need of a business card for our dynamic company expanding its customer base and need to be easily contacted and identified for when we visit with government officials, potential EMS / Fire agencies and county coordinators to arrange for training programs for first responders to better prepare them for critical thinking at critical incidents.

Target Market(s)

EMS/Fire and Event Promoters

Industry/Entity Type

Medical

Contact Information for Business Card

Two cards, comparable designs:

Martin K. Halvey, Principal, m.halvey@rvqtlo.com
Owen Tash, Event and Training Specialist, o.tash@rvqtlo.com

Font styles to use
Other font styles liked:
• Cambria

Colors

Designer to choose colors to be used in the design.

Requirements
Must have
• Company Logo, Spots for Name, Title, Phone Number, Email, Website
• A bullet list stating that we offer, QRB CPR and First Aid Instructors, Hold the Line Instructors, Event EMS, CME's, MCI Training and Planning. We prefer to have a black background for the card but if you can make a blue or white card stand out we would review that as well.
Should not have
• Tacky logos or special sayings ... simple, elegant, professional is the look we seek

```html
<!DOCTYPE html>
<html lang="en">
<head>
<meta charset="utf-8">
<title>RVQ Training Co. – Business Card</title>
<link rel="stylesheet" href="https://fonts.googleapis.com/css2?family=Roboto:wght@400;500;700&display=swap">
<style>
  :root {
    --navy: #0b1850;
    --red: #d0252c;
    --white: #ffffff;
    --ink-grey: #5d6270;
    --backdrop: #e9e9ec;
  }
  * { box-sizing: border-box; margin: 0; padding: 0; }
  html, body {
    width: 1200px; height: 1200px; overflow: hidden;
    background: var(--backdrop);
    font-family: "Roboto", Arial, sans-serif;
  }
  .card {
    position: absolute; left: 213px; width: 774px; height: 442px;
    overflow: hidden;
    box-shadow: 0 4px 14px rgba(0,0,0,0.18);
  }
  .card-front { top: 149px; background: var(--white); }
  .card-back { top: 633px; background: var(--navy); color: var(--white); }

  .wordmark {
    font-weight: 700; letter-spacing: 1px; line-height: 1;
  }
  .card-front .wordmark {
    position: absolute; left: 41px; top: 48px;
    font-size: 40px; color: var(--navy);
  }
  .front-emblem {
    position: absolute; right: -70px; top: 75px;
    width: 330px; height: 330px;
  }
  .identity { position: absolute; left: 41px; top: 183px; }
  .person-name { font-size: 27px; font-weight: 500; color: var(--navy); }
  .person-title { font-size: 20px; color: var(--ink-grey); margin-top: 4px; }
  .postal {
    position: absolute; left: 41px; top: 262px;
    font-size: 19px; line-height: 27px; color: var(--ink-grey);
  }
  .contact-list {
    position: absolute; left: 41px; top: 332px; list-style: none;
    font-size: 19px; line-height: 27px; color: var(--ink-grey);
  }
  .contact-list li { display: flex; align-items: center; gap: 12px; }
  .contact-list svg { width: 16px; height: 16px; fill: var(--navy); flex: none; }

  .brand-lockup {
    position: absolute; left: 0; right: 0; top: 168px;
    display: flex; justify-content: center; align-items: center; gap: 18px;
  }
  .brand-dot { width: 46px; height: 46px; border-radius: 50%; background: var(--white); }
  .card-back .wordmark { font-size: 46px; color: var(--white); }
  .services {
    position: absolute; left: 0; right: 0; top: 359px;
    text-align: center; font-size: 19px; line-height: 29px;
  }
  .services span { margin: 0 6px; }
  .services span::before {
    content: "•"; color: var(--red); margin-right: 7px;
  }
</style>
</head>
<body>
  <section class="card card-front">
    <div class="wordmark">RVQ Training Co.</div>

    <svg class="front-emblem" viewBox="0 0 100 100" aria-hidden="true">
      <circle cx="50" cy="50" r="50" fill="#0b1850"/>
    </svg>

    <div class="identity">
      <div class="person-name">Martin K. Halvey</div>
      <div class="person-title">Principal</div>
    </div>
    <address class="postal" style="font-style:normal">
      PO BOX 418<br>Marrowfield NY 12990
    </address>
    <ul class="contact-list">
      <li>
        <svg viewBox="0 0 24 24"><path d="M6.6 10.8a15.1 15.1 0 0 0 6.6 6.6l2.2-2.2a1 1 0 0 1 1-.25 11.4 11.4 0 0 0 3.6.57 1 1 0 0 1 1 1V20a1 1 0 0 1-1 1A17 17 0 0 1 3 4a1 1 0 0 1 1-1h3.5a1 1 0 0 1 1 1c0 1.25.2 2.45.57 3.57a1 1 0 0 1-.25 1z"/></svg>
        (555) 014 2288
      </li>
      <li>
        <svg viewBox="0 0 24 24"><path d="M2 5h20v14H2z M4 7v.5l8 5 8-5V7l-8 5z" fill-rule="evenodd"/></svg>
        m.halvey@rvqtlo.com
      </li>
      <li>
        <svg viewBox="0 0 24 24"><path d="M12 2a10 10 0 1 0 0 20 10 10 0 0 0 0-20zm6.9 6h-3a15.6 15.6 0 0 0-1.4-3.6A8 8 0 0 1 18.9 8zM12 4c.8 1.2 1.5 2.5 1.9 4h-3.8c.4-1.5 1.1-2.8 1.9-4zM4.3 14a8 8 0 0 1 0-4h3.4a16 16 0 0 0 0 4zm.8 2h3a15.6 15.6 0 0 0 1.4 3.6A8 8 0 0 1 5.1 16zm3-8h-3a8 8 0 0 1 4.4-3.6A15.6 15.6 0 0 0 8.1 8zM12 20c-.8-1.2-1.5-2.5-1.9-4h3.8c-.4 1.5-1.1 2.8-1.9 4zm2.3-6H9.7a14.7 14.7 0 0 1 0-4h4.6a14.7 14.7 0 0 1 0 4zm.2 5.6a15.6 15.6 0 0 0 1.4-3.6h3a8 8 0 0 1-4.4 3.6zm1.8-5.6a16 16 0 0 0 0-4h3.4a8 8 0 0 1 0 4z"/></svg>
        www.rvqtlo.com
      </li>
    </ul>
  </section>

  <section class="card card-back">
    <div class="brand-lockup">
      <div class="brand-dot"></div>
      <div class="wordmark">RVQ Training Co.</div>
    </div>
    <p class="services">
      <span>we have QRB CPR</span><span>First Aid Instructors</span><span>Hold the Line Instructors</span><br>
      <span>we do Event EMS, CME's, MCI Training and Planning</span>
    </p>
  </section>
</body>
</html>
```